Computer Company needs a Business card design

We need a business card design for our business. We assist people to transition to the QLX (Quorra Linkwave Exchange). The Australian Government-owned qlx™ network is a brand new telecommunications network currently being rolled out across Australia, giving access to a reliable broadband connection. Our niche market will predominantly be domestic customers in the 50+ age bracket. The assistance that we provide is everything from arranging the equipment, arranging the plan and contract term, appointment times, final testing of the network and any tweaks that need to be made. We basically PM the transition from start to finish. The business card design should be minimalist, should communicate loyalty and stability, should be easy to read and clearly explain what we do. We have asked for front and back. However, the back of the card does not have to include much information at all. It could be just a small design, or a repeat of our phone number. Up to you. The attached file only says what is required on the card. It does not specify where to arrange the text, what fonts to use, etc etc. As much as we would like to give you more info, due to our very limited design ability, we are not really able to send you any rough, or otherwise, designs of what we are after. Hopefully the above description is enough for you.

```html
<!DOCTYPE html>
<html lang="en">
<head>
<meta charset="utf-8">
<title>Linkwise Home – Business Card</title>
<link rel="stylesheet" href="https://fonts.googleapis.com/css2?family=Questrial&family=Poppins:wght@600&display=swap">
<style>
  :root {
    --backdrop: #d4d4d4;
    --brand-blue: #0a86ad;
    --brand-orange: #f08410;
    --card-white: #f3f3f3;
    --text-white: #ffffff;
  }
  * { margin: 0; padding: 0; box-sizing: border-box; }
  html, body {
    width: 1200px;
    height: 960px;
    overflow: hidden;
    background: var(--backdrop);
  }
  .canvas {
    position: relative;
    width: 1200px;
    height: 960px;
  }
  .card {
    position: absolute;
    left: 320px;
    width: 602px;
    height: 342px;
    box-shadow: 0 3px 8px rgba(0, 0, 0, 0.25);
  }
  .card-front {
    top: 106px;
    background: var(--brand-blue);
    display: flex;
    align-items: center;
    justify-content: center;
  }
  .business-name {
    font-family: "Poppins", sans-serif;
    font-weight: 600;
    white-space: nowrap;
  }
  .card-front .business-name {
    font-size: 50px;
    color: var(--text-white);
    transform: translate(1px, 4px);
  }
  .card-back {
    top: 493px;
    display: flex;
  }
  .back-brand {
    width: 298px;
    height: 100%;
    background: var(--card-white);
    display: flex;
    align-items: center;
    justify-content: center;
  }
  .back-brand .business-name {
    font-size: 30px;
    color: var(--brand-blue);
    transform: translate(-2px, 4px);
  }
  .divider {
    width: 4px;
    height: 100%;
    background: var(--brand-orange);
  }
  .back-contact {
    flex: 1;
    background: var(--brand-blue);
    color: var(--text-white);
    padding: 112px 0 0 27px;
  }
  .person-name {
    font-family: "Poppins", sans-serif;
    font-weight: 600;
    font-size: 21px;
    letter-spacing: 1px;
    line-height: 1.2;
  }
  .person-role {
    font-family: "Questrial", sans-serif;
    font-size: 16px;
    letter-spacing: 0.5px;
    margin-top: 1px;
  }
  .contact-list {
    list-style: none;
    margin-top: 13px;
    font-family: "Questrial", sans-serif;
    font-size: 15.5px;
    letter-spacing: 0.3px;
  }
  .contact-list li {
    display: flex;
    align-items: center;
    gap: 8px;
    height: 19.5px;
  }
  .contact-list svg {
    width: 13px;
    height: 13px;
    fill: var(--text-white);
    flex: none;
  }
</style>
</head>
<body>
<main class="canvas">
  <section class="card card-front" aria-label="Card front">
    <div class="business-name">Linkwise Home</div>
  </section>

  <section class="card card-back" aria-label="Card back">
    <div class="back-brand">
      <div class="business-name">Linkwise Home</div>
    </div>
    <div class="divider"></div>
    <div class="back-contact">
      <h1 class="person-name">DEAN HARLOW</h1>
      <p class="person-role">CEO/FOUNDER</p>
      <ul class="contact-list">
        <li>
          <svg viewBox="0 0 24 24" aria-hidden="true"><path d="M6.6 10.8a15.1 15.1 0 0 0 6.6 6.6l2.2-2.2a1 1 0 0 1 1-.25 11.4 11.4 0 0 0 3.6.57 1 1 0 0 1 1 1V20a1 1 0 0 1-1 1A17 17 0 0 1 3 4a1 1 0 0 1 1-1h3.5a1 1 0 0 1 1 1c0 1.25.2 2.46.57 3.6a1 1 0 0 1-.25 1z"/></svg>
          <span>0412558930</span>
        </li>
        <li>
          <svg viewBox="0 0 24 24" aria-hidden="true"><path d="M2 5h20v14H2zm2 2v.4l8 5.1 8-5.1V7zm0 2.8V17h16V9.8l-8 5.1z"/></svg>
          <span>dean@linkwisehome.com.au</span>
        </li>
        <li>
          <svg viewBox="0 0 24 24" aria-hidden="true"><path d="M12 2a10 10 0 1 0 0 20 10 10 0 0 0 0-20zm-1 17.9A8 8 0 0 1 4.2 10.2L9 15v1a2 2 0 0 0 2 2zm6.9-2.5A2 2 0 0 0 16 16h-1v-3a1 1 0 0 0-1-1H8v-2h2a1 1 0 0 0 1-1V7h2a2 2 0 0 0 2-2v-.4a8 8 0 0 1 2.9 12.8z"/></svg>
          <span>www.linkwisehome.com.au</span>
        </li>
      </ul>
    </div>
  </section>
</main>
</body>
</html>
```